Brightwell Homes Guide Business card

I have had at the logo designed here and attached. The business compares off the plan apartments in Sydney and provides quick comparison for new home buyers e.g price, floor plans and location. I would like the complimentary colours used on the business card. I would like it be unique but also look professional. I also have a website to gain inspiration from www.brightwellhomesguide.com.au
Updates
Industry/Entity Type
Business
Contact Information for Business Card
Helen Vostrakis
Director of Business Development
e: helen.vostrakis@brightwellhomesguide.com.au
p: (02) 8143 7692
m: 0431 572 908
w: www.brightwellhomesguide.com.au
Look and feel
Each slider illustrates characteristics of the customer's brand and the style your logo design should communicate.

```html
<!DOCTYPE html>
<html lang="en">
<head>
<meta charset="utf-8">
<title>Brightwell Homes Guide — Business Card</title>
<link rel="stylesheet" href="https://fonts.googleapis.com/css2?family=Open+Sans:wght@400;600&display=swap">
<style>
  :root {
    --stage: #e9e7e3;
    --card-dark: #3b3b3c;
    --card-dark-edge: #2e2e2f;
    --brand-green: #8cc63f;
    --brand-blue: #2f95d0;
    --paper: #f4f4f4;
    --ink: #3a3a3a;
    --white: #ffffff;
  }
  * { margin: 0; padding: 0; box-sizing: border-box; }
  html, body { width: 1200px; height: 1200px; overflow: hidden; }
  body {
    background: var(--stage);
    font-family: "Open Sans", Arial, sans-serif;
    position: relative;
  }
  .card {
    position: absolute;
    left: 150px;
    width: 900px;
    height: 514px;
    border-radius: 4px;
    overflow: hidden;
    box-shadow: 0 10px 28px rgba(0,0,0,0.22);
    background: linear-gradient(160deg, var(--card-dark) 0%, var(--card-dark-edge) 100%);
  }
  .card--front { top: 50px; }
  .card--back { top: 636px; }

  .wordmark {
    display: flex;
    align-items: center;
    gap: 18px;
    color: var(--brand-green);
    font-weight: 600;
    white-space: nowrap;
  }
  .wordmark__square {
    background: var(--brand-blue);
    flex: none;
  }
  .card--front .wordmark {
    position: absolute;
    left: 0; right: 0; top: 200px;
    justify-content: center;
    font-size: 56px;
  }
  .card--front .wordmark__square { width: 58px; height: 58px; }
  .front__url {
    position: absolute;
    left: 0; right: 0; bottom: 34px;
    text-align: center;
    color: var(--white);
    font-size: 20px;
    letter-spacing: 0.3px;
  }

  .back__art { position: absolute; inset: 0; }
  .card--back .wordmark {
    position: absolute;
    left: 40px; top: 48px;
    font-size: 34px;
    gap: 12px;
  }
  .card--back .wordmark__square { width: 36px; height: 36px; }
  .contact {
    position: absolute;
    left: 470px; top: 218px;
    color: var(--ink);
  }
  .contact__name { color: var(--brand-green); font-size: 30px; font-weight: 400; line-height: 1.2; }
  .contact__role { font-size: 20px; margin-top: 2px; }
  .contact__list { list-style: none; margin-top: 62px; font-size: 20px; }
  .contact__list li { display: flex; align-items: center; gap: 12px; height: 34px; }
  .contact__icon { width: 22px; height: 18px; flex: none; }
  .social {
    position: absolute;
    left: 628px; top: 444px;
    display: flex; gap: 10px;
  }
  .social__dot { width: 22px; height: 22px; border-radius: 4px; background: var(--brand-green); }
</style>
</head>
<body>

  <section class="card card--front" aria-label="Business card front">
    <div class="wordmark"><span class="wordmark__square"></span>Brightwell Homes Guide</div>
    <p class="front__url">www.brightwellhomesguide.com.au</p>
  </section>

  <section class="card card--back" aria-label="Business card back">
    <svg class="back__art" viewBox="0 0 900 514" width="900" height="514" aria-hidden="true">
      <polygon points="260,514 260,377 560,60 900,185 900,514" fill="var(--paper)"/>
      <polyline points="118,526 560,48 912,178" fill="none" stroke="var(--brand-green)" stroke-width="26" stroke-linejoin="miter"/>
      <line x1="258" y1="380" x2="258" y2="514" stroke="var(--brand-green)" stroke-width="12"/>
    </svg>

    <div class="wordmark"><span class="wordmark__square"></span>Brightwell Homes Guide</div>

    <div class="contact">
      <h1 class="contact__name">Tom Ellery</h1>
      <p class="contact__role">Managing Partner</p>
      <ul class="contact__list">
        <li>
          <svg class="contact__icon" viewBox="0 0 22 18" aria-label="Phone">
            <path d="M2 6 Q11 -1 20 6 L17 9 L14 7 L14 5 Q11 4 8 5 L8 7 L5 9 Z" fill="var(--brand-blue)"/>
            <rect x="5" y="10" width="12" height="7" rx="2" fill="var(--brand-blue)"/>
          </svg>
          000.000.0000
        </li>
        <li>
          <svg class="contact__icon" viewBox="0 0 22 18" aria-label="Email">
            <rect x="1" y="2" width="20" height="14" rx="1.5" fill="var(--brand-blue)"/>
            <polyline points="1.5,3 11,10 20.5,3" fill="none" stroke="var(--paper)" stroke-width="1.6"/>
          </svg>
          tellery@brightwellhomesguide.com.au
        </li>
      </ul>
    </div>

    <div class="social" aria-label="Social links">
      <span class="social__dot"></span>
      <span class="social__dot"></span>
    </div>
  </section>

</body>
</html>
```